Website for IT consulting Company

I need a website upgrade, the existing site content is ok, I would also like to add a testimonial page, the site should be something that is easy for us to update content. You use the content from www.kavnex.com as an example. I will also post update logo and artwork. I also need a contact form with some type of validation or captcha.

I added Coded to the Project

Please omit Address maps

Target Market(s)

small business, service oriented companies. We provide IT Consulting, support and mangement

Industry/Entity Type

Information Technology

Coding

Coded - Design and coding required

Number of Pages Required

1 page

Font styles to use
Serif
Sans Serif

Requirements
Must have
• Contain logo attached, and content from existing web site www.kavnex.com.
• Also need to update content easily, and be movable to different platforms.
• There is a catch phrase
• "Let us worry about your technology…” “ so you don’t have to!”
• Should be included.
Nice to have
• Testimonial page, Project page where we can post new and past projects and pictures
Should not have
• none

```html
<!DOCTYPE html>
<html lang="en">
<head>
<meta charset="utf-8">
<title>Kavnex Development Group</title>
<link href="https://fonts.googleapis.com/css2?family=Roboto:ital,wght@0,400;0,500;0,700;1,400&family=Shadows+Into+Light+Two&display=swap" rel="stylesheet">
<style>
:root{
  --orange:#ed7d17;
  --orange-soft:#f0954a;
  --ink:#222;
  --text:#444;
  --muted:#777;
  --bar:#eceef1;
  --light:#f4f5f7;
  --footer:#6d6e71;
  --white:#fff;
}
*{box-sizing:border-box;margin:0;padding:0}
html,body{width:690px;height:1200px;overflow:hidden;background:var(--white)}
body{font-family:"Roboto",Arial,sans-serif;color:var(--text)}
.page{width:690px;height:1200px;position:relative;overflow:hidden}

.site-header{height:42px;border-top:2px solid var(--orange);display:flex;align-items:center;justify-content:space-between;padding:0 28px;background:var(--white)}
.brand{display:flex;align-items:center;gap:6px;font-weight:700;font-size:20px;color:var(--orange);letter-spacing:1px}
.brand-mark{width:16px;height:16px;background:var(--orange)}
.main-nav{display:flex;gap:21px;font-size:8px;font-weight:500;color:var(--ink)}
.main-nav .active{color:var(--orange)}

.hero{height:283px;position:relative;background:linear-gradient(120deg,#5a5652 0%,#3d3a38 45%,#6a6460 100%);display:flex;flex-direction:column;align-items:center;justify-content:center}
.hero-tagline{font-family:"Shadows Into Light Two",cursive;color:var(--white);font-size:18px;text-align:center;line-height:27px;letter-spacing:1px}
.hero-btn{margin-top:10px;border:1px solid rgba(255,255,255,.8);border-radius:4px;color:var(--white);font-size:7px;padding:5px 11px}

.info-bar{height:18px;background:var(--bar);display:flex;align-items:center;justify-content:space-between;padding:0 30px;font-size:7.5px;color:var(--muted)}
.info-bar .contact{display:flex;gap:16px;align-items:center}
.info-bar .item{display:flex;gap:4px;align-items:center}
.info-bar .social{display:flex;gap:8px;align-items:center}
.info-bar .dot{width:10px;height:10px;border-radius:2px;background:#9a9ea5}

.section-title{font-size:13px;font-weight:700;color:var(--ink);text-align:center}
.section-title span{color:var(--orange)}
.rule{border-top:1px dashed var(--orange);margin:8px 30px 0}

.welcome{height:82px;padding-top:9px}
.welcome p{font-size:6.6px;line-height:11px;text-align:center;color:var(--text);padding:8px 36px 0}

.solutions{height:165px;background:var(--light);padding-top:12px}
.solutions .rule{margin-bottom:11px}
.service-list{display:flex;justify-content:space-between;padding:0 35px}
.service{width:81px;text-align:center}
.service-photo{width:81px;height:81px;border-radius:50%}
.service-name{margin-top:5px;font-size:10.5px;line-height:13px;color:var(--ink);font-weight:500}
.p1{background:radial-gradient(circle,#6f7d8a,#2c3a48)}
.p2{background:radial-gradient(circle,#4f7fb8,#1e3f6e)}
.p3{background:radial-gradient(circle,#b59a82,#5c4a3e)}
.p4{background:radial-gradient(circle,#cfc9c2,#4a4642)}
.p5{background:radial-gradient(circle,#d8d8d6,#7a7d80)}
.p6{background:radial-gradient(circle,#a7a29c,#4e4b48)}

.offers{height:141px;display:flex}
.offer{flex:1;color:var(--white);text-align:center;padding:13px 18px 0}
.offer h3{font-size:15.5px;line-height:15.5px;font-weight:700}
.offer p{font-size:7.6px;line-height:13px;margin-top:13px}
.offer.soft{background:var(--orange-soft)}
.offer.strong{background:var(--orange)}

.testimonials{height:199px;background:var(--light);padding-top:11px}
.quote-grid{display:grid;grid-template-columns:1fr 1fr;margin:0 30px}
.quote{display:flex;align-items:center;gap:13px;height:80px;padding:0 8px}
.quote.left{border-right:1px dashed #aaa;justify-content:flex-end;text-align:right}
.quote.top{border-bottom:1px dashed #aaa}
.quote-text{font-size:6.8px;line-height:11px;font-style:italic;color:var(--muted)}
.quote-author{font-size:7px;color:var(--ink);font-style:normal;margin-top:5px}
.avatar{width:44px;height:44px;border-radius:50%;flex:none;background:radial-gradient(circle,#d9c2ae,#8b6f5c)}

.likes{height:42px;display:flex;align-items:center;justify-content:center;position:relative}
.likes::before{content:"";position:absolute;left:36px;right:36px;top:21px;border-top:1px solid #e2e2e2}
.like-box{position:relative;width:258px;height:28px;border:1px solid #ddd;border-radius:14px;background:var(--white);display:flex;align-items:center}
.like-thumb{width:34px;height:100%;border-right:1px solid #ddd;display:flex;align-items:center;justify-content:center}
.like-btn{margin-left:36px;background:#4a6ea9;color:var(--white);font-size:6px;font-weight:700;padding:2px 5px;border-radius:2px}
.like-text{font-size:5.5px;margin-left:4px;color:var(--ink)}

.site-footer{height:228px;background:var(--footer);color:var(--white);padding:13px 30px 0}
.footer-cols{display:flex;gap:12px;height:175px}
.footer-col h4{font-size:10.5px;font-weight:700;margin-bottom:10px}
.col-contact{width:150px;font-size:7px;line-height:11.5px}
.col-contact p{margin-bottom:8px}
.col-mail{flex:1;padding:0 4px}
.col-mail h4{text-align:center}
.field{background:var(--white);border-radius:2px;height:18px;font-size:6.6px;color:#999;padding:5px 8px}
.field-row{display:flex;gap:12px;margin-bottom:8px}
.field-row .field{flex:1}
.field.wide{margin-bottom:8px}
.field.msg{height:36px}
.send-btn{display:block;margin:12px auto 0;width:78px;height:18px;background:var(--white);color:var(--ink);font-size:6.8px;font-weight:500;text-align:center;line-height:18px;border-radius:2px}
.col-about{width:146px;font-size:7px;line-height:11.5px}
.col-about p{margin-bottom:8px}
.foot-icons{display:flex;gap:8px;margin-top:4px}
.foot-icons span{width:7px;height:7px;border-radius:50%;background:var(--white)}
.footer-bottom{border-top:1px solid #9a9b9e;height:40px;display:flex;align-items:center;justify-content:space-between;font-size:6.5px;font-weight:700}
.footer-brand{font-size:16px;color:var(--white);display:flex;gap:5px;align-items:center;letter-spacing:1px}
.footer-brand i{width:12px;height:12px;background:var(--white)}
</style>
</head>
<body>
<div class="page">

<header class="site-header">
  <div class="brand"><span class="brand-mark"></span>KAVNEX</div>
  <nav class="main-nav">
    <span class="active">HOME</span><span>ABOUT</span><span>SUPPORT</span><span>CLIENTS</span><span>PROJECT</span><span>CAREERS</span><span>CONTACT</span>
  </nav>
</header>

<section class="hero" role="img" aria-label="Team of three colleagues talking in an office, darkened background photo">
  <p class="hero-tagline">Let us worry about your technology...<br>so you don't have to!</p>
  <span class="hero-btn">Get Started</span>
</section>

<div class="info-bar">
  <div class="contact">
    <span class="item"><svg width="8" height="8" viewBox="0 0 10 10"><path d="M2 1l2 2-1 1.5c.8 1.5 1.8 2.5 3.3 3.3L7.8 6.8l2 2L8.5 10C4 9.5.5 6 0 1.5z" fill="#888"/></svg>+1 800 555 01 72</span>
    <span class="item"><svg width="9" height="7" viewBox="0 0 10 8"><rect width="10" height="8" fill="#888"/><path d="M0 0l5 4 5-4" stroke="#eceef1" fill="none"/></svg>hello@kavnex.com</span>
  </div>
  <div class="social">
    <span class="dot"></span><span class="dot"></span><span class="dot"></span>
    <svg width="9" height="9" viewBox="0 0 10 10"><circle cx="4" cy="4" r="3" stroke="#888" stroke-width="1.4" fill="none"/><path d="M6.2 6.2L9.5 9.5" stroke="#888" stroke-width="1.5"/></svg>
  </div>
</div>

<section class="welcome">
  <h2 class="section-title">Welcome to <span>Kavnex Development Group, INC</span></h2>
  <div class="rule"></div>
  <p>Kavnex is a technology solution provider based in Houston, Texas. Our goal is to make technology a non-issue for individuals and small to medium size businesses ranging from 5 to 150 Users. Kavnex has the experience, the tools, high-level technology solutions and training to power your business and your work force. We understand that all business's have one goal in common! (KDG) A Return on Investment</p>
</section>

<section class="solutions">
  <h2 class="section-title">IT Support <span>Solutions</span></h2>
  <div class="rule"></div>
  <div class="service-list">
    <div class="service"><div class="service-photo p1" role="img" aria-label="Technician in a server room"></div><div class="service-name">NETWORK<br>Administration</div></div>
    <div class="service"><div class="service-photo p2" role="img" aria-label="Blue network cables in a patch panel"></div><div class="service-name">NETWORK<br>Cabling</div></div>
    <div class="service"><div class="service-photo p3" role="img" aria-label="Office workers with a security shield overlay"></div><div class="service-name">NETWORK<br>Security</div></div>
    <div class="service"><div class="service-photo p4" role="img" aria-label="Hand near a wireless router"></div><div class="service-name">WIRELESS<br>Networks</div></div>
    <div class="service"><div class="service-photo p5" role="img" aria-label="Man at a desk with an eye icon overlay"></div><div class="service-name">ANTIVIRUS<br>Solutions</div></div>
    <div class="service"><div class="service-photo p6" role="img" aria-label="Colleagues around a desktop monitor"></div><div class="service-name">DESKTOP<br>Support</div></div>
  </div>
</section>

<section class="offers">
  <div class="offer soft"><h3>IT Infrastructure Design and Installation</h3><p>Do you have more than one site? Do you need remote access? We can design and implement LANS/WANS and VPN's. Make your important data available to you wherever you are.</p></div>
  <div class="offer strong"><h3>Managed IT<br>Solutions</h3><p>Our staff will design, service, administer and maintain your IT needs.<br>We are well versed on all major operating system, and network appliances</p></div>
  <div class="offer soft"><h3>Remote Diagnostic and Support</h3><p>Do you need a quick solution to a technical problem? With our live remote-assistance tool, a member of our support team can view your desktop and control of your mouse and keyboard to get you on your way to a solution.</p></div>
</section>

<section class="testimonials">
  <h2 class="section-title">What <span>People Say</span></h2>
  <div class="rule" style="margin-bottom:6px"></div>
  <div class="quote-grid">
    <div class="quote left top"><div><p class="quote-text">Duis aute irure dolor in reprehenderit in voluptate velit esse cillum dolore eu fugiat nulla pariatur. Excepteur sint occaecat cupidatat non proident, sunt in culpa qui officia deserunt mollit.</p><p class="quote-author">Owen Marsh, Operations Manager</p></div><div class="avatar" role="img" aria-label="Portrait photo of client"></div></div>
    <div class="quote top"><div class="avatar" role="img" aria-label="Portrait photo of client"></div><div><p class="quote-text">Provident, similique sunt in culpa qui officia deserunt mollitia animi, id est laborum et dolorum fuga. Et harum quidem rerum facilis est et expedita distinctio. Nam libero tempore, cum soluta nobis.</p><p class="quote-author">Nora Bellis, Creative Designer</p></div></div>
    <div class="quote left"><div><p class="quote-text">Luis aute irure dolor in reprehenderit in pluptate velit esse cillum dolore eu fugiat nulla pariatur. Excepteur sint occaecat cupidatat non proident, sunt in culpa qui officia deserunt mollit.</p><p class="quote-author">Tessa Quill, Manager</p></div><div class="avatar" role="img" aria-label="Portrait photo of client"></div></div>
    <div class="quote"><div class="avatar" role="img" aria-label="Portrait photo of client"></div><div><p class="quote-text">At vero eos et accusamus et iusto odio dignissimos ducimus qui blanditiis praesentium voluptatum deleniti atque corrupti quos dolores et quas molestias excepturi sint occaecati asperiores.</p><p class="quote-author">Evan Rusk, Developer</p></div></div>
  </div>
</section>

<div class="likes">
  <div class="like-box">
    <div class="like-thumb"><svg width="11" height="11" viewBox="0 0 12 12"><path d="M1 5h2v6H1zM4 5l2.5-4c1 0 1.5.7 1.2 1.8L7.3 4.5H11l-1 6.5H4z" fill="none" stroke="#bbb"/></svg></div>
    <span class="like-btn">&#10003; Like</span><span class="like-text">You and 4k others like this.</span>
  </div>
</div>

<footer class="site-footer">
  <div class="footer-cols">
    <div class="footer-col col-contact">
      <h4>Contact Us</h4>
      <p>Please feel free to contact us for any issue. Our staff is available to you from 9AM until 5PM on weekdays.</p>
      <p><b>Phone:</b> +1 (713) 555-0148</p>
      <p><b>Office:</b> 1187 Larkmoor Ave. Houston, TX 77099</p>
      <p><b>Email:</b> info@kavnexgroup.com</p>
      <div class="foot-icons"><span></span><span></span><span></span><span></span><span></span></div>
    </div>
    <div class="footer-col col-mail">
      <h4>Feel Free to Mail</h4>
      <div class="field-row"><div class="field">Name *</div><div class="field">Email *</div></div>
      <div class="field wide">Subject</div>
      <div class="field msg">Write Your Message Here...</div>
      <span class="send-btn">SEND MESSAGE</span>
    </div>
    <div class="footer-col col-about">
      <h4>About Team</h4>
      <p>Enim congue blandit. Lorem ipsum dolor sit amet, consectetur adipiscing elit. Quisque consectetur interdum finibus. Vestibulum ante ipsum primis in faucibus orci. luctus et ultrices posuere.</p>
      <p>Cubilia cras blandit finibus ipsum, id porttitor arcu volutpat a. Integer iaculis erat nec justo malesuada faucibus vel tempus sapien. Vivamus aliquam euismod tristique.</p>
    </div>
  </div>
  <div class="footer-bottom">
    <span>© 2007 - 2017 Kavnex Development Group, Inc</span>
    <span class="footer-brand"><i></i>KAVNEX</span>
    <span>All rights reserved</span>
  </div>
</footer>

</div>
</body>
</html>
```